Pebble Grocer

Hope all is well!

Wanted to make business cards for my father. His name is Samir Haddad and owns convenience stores. I have attached logo :)

He does not want any title just simple name and phone. An email would be nice as well.

Samir Haddad
Cell: 413-555-0148
Store: 413-555-0192

Pebblegrocer518@mailnest.example

The design and style is totally up to you :) The colors we were looking for were the same as logo :)

```html
<!DOCTYPE html>
<html lang="en">
<head>
<meta charset="utf-8">
<title>Pebble Grocer – Business Card</title>
<link rel="stylesheet" href="https://fonts.googleapis.com/css2?family=Tinos:wght@700&family=Mulish:wght@500&display=swap">
<style>
  :root {
    --backdrop: #d3d4d6;
    --card: #ffffff;
    --navy: #253a7a;
    --red: #ec3237;
  }
  * { margin: 0; padding: 0; box-sizing: border-box; }
  html, body { width: 900px; height: 1200px; overflow: hidden; }
  body { background: var(--backdrop); position: relative; }

  .card {
    position: absolute;
    left: 133px;
    width: 633px;
    height: 364px;
    background: var(--card);
  }
  .card--front { top: 210px; }
  .card--back { top: 624px; }

  .brand-name {
    position: absolute;
    left: 0; right: 0;
    top: 148px;
    text-align: center;
    font-family: "Tinos", "Times New Roman", serif;
    font-weight: 700;
    font-size: 58px;
    line-height: 1;
    color: var(--navy);
  }

  .holder {
    position: absolute;
    left: 36px;
    top: 150px;
    width: 263px;
  }
  .holder-name {
    font-family: "Tinos", "Times New Roman", serif;
    font-weight: 700;
    font-size: 28px;
    line-height: 1;
    letter-spacing: 0.5px;
    color: var(--navy);
    text-transform: uppercase;
  }
  .holder-rules { display: block; margin-top: 12px; }

  .divider {
    position: absolute;
    left: 316px;
    top: 150px;
    width: 3px;
    height: 67px;
    background: var(--navy);
  }

  .contact {
    position: absolute;
    left: 333px;
    top: 148px;
    list-style: none;
    font-family: "Mulish", "Helvetica", sans-serif;
    font-weight: 500;
    color: var(--navy);
  }
  .contact li { height: 26px; line-height: 26px; white-space: nowrap; }
  .contact .label { color: var(--red); }
  .contact .phone { font-size: 19px; letter-spacing: 3px; }
  .contact .email { font-size: 15.5px; }
</style>
</head>
<body>
  <section class="card card--front">
    <h1 class="brand-name">Pebble Grocer</h1>
  </section>

  <section class="card card--back">
    <div class="holder">
      <p class="holder-name">Samir Haddad</p>
      <svg class="holder-rules" width="263" height="15" viewBox="0 0 263 15" aria-hidden="true">
        <rect x="0" y="0" width="263" height="3" fill="var(--red)"/>
        <rect x="0" y="6" width="263" height="3" fill="var(--red)"/>
        <rect x="0" y="12" width="263" height="3" fill="var(--red)"/>
      </svg>
    </div>

    <div class="divider"></div>

    <ul class="contact">
      <li class="phone"><span class="label">C:</span>413-555-0148</li>
      <li class="phone"><span class="label">S:</span>413-555-0192</li>
      <li class="email"><span class="label">E:</span> Pebblegrocer518@mailnest.example</li>
    </ul>
  </section>
</body>
</html>
```